Cover design for inventory booklets

As a company we have used a front cover to all our reports which need to include specific information about each property
We therefore need an A4 design design which must allow for inclusion of of the following editable elements through Microsoft Word although I am happy to embed graphical content into Word if not done as part of design process:
Property picture (or pictures if design allows)
Property address
Property size
Agent name (can include logo insert as well if you want)
Job type
Job date
We would like something which appears professional but also acts as a sales tool for the company and repeat business so inclusion of contact details in some form is essential
Style and colours should be derived and be reasonably consistent with those found in our website potentially included the blue tones from the logo and the green of the website as contrast at http://www.quillbrookstays.co.uk/ although please do not let this constrain the designs submitted as we will provide feedback as needed
Target Market(s)
Primary - Letting Agents, Secondary - Landlords and Tenants
Industry/Entity Type
Business

```html
<!DOCTYPE html>
<html lang="en">
<head>
<meta charset="utf-8">
<title>Quillbrook Stays – Inventory Report Cover</title>
<link href="https://fonts.googleapis.com/css2?family=Source+Sans+3:wght@400;600;700&display=swap" rel="stylesheet">
<style>
  :root {
    --navy: #23205f;
    --royal: #1f55a8;
    --heading-blue: #1f4fa3;
    --ink: #2b2b33;
    --paper: #f4f5f7;
    --paper-light: #ffffff;
    --rule: #cfd3da;
    --photo-sky: #6fa6dc;
    --photo-brick: #8a4a34;
    --photo-green: #3d6b2c;
  }
  * { margin: 0; padding: 0; box-sizing: border-box; }
  html, body { width: 844px; height: 1200px; overflow: hidden; background: var(--paper); }
  body { font-family: "Source Sans 3", sans-serif; color: var(--ink); }

  .cover {
    position: relative;
    width: 844px;
    height: 1200px;
    overflow: hidden;
    background: linear-gradient(180deg, var(--paper-light) 560px, var(--paper) 1200px);
  }

  .header-band {
    position: absolute; left: 0; top: 0;
    width: 844px; height: 620px;
  }

  .brand-name {
    position: absolute; left: 0; top: 160px; width: 844px;
    text-align: center;
    font-size: 58px; font-weight: 400; letter-spacing: 2px;
    color: #ffffff; line-height: 1;
  }

  .contact {
    position: absolute; left: 0; top: 268px; width: 844px;
    text-align: center; color: #ffffff;
    font-size: 15px; line-height: 19px;
  }
  .contact .gap { height: 7px; }

  .web {
    position: absolute; left: 277px; top: 384px; width: 290px; height: 31px;
    text-align: center; color: #ffffff; font-size: 17px; line-height: 31px;
    letter-spacing: 0.3px;
    border-top: 1px solid rgba(255,255,255,0.35);
    border-bottom: 1px solid rgba(255,255,255,0.35);
  }
  .web strong { font-weight: 700; }

  .photo {
    position: absolute;
    border: 2px solid var(--heading-blue);
    box-shadow: 0 10px 12px -10px rgba(0,0,0,0.35);
  }
  .photo-main {
    left: 69px; top: 653px; width: 461px; height: 289px;
    background: linear-gradient(160deg, var(--photo-sky) 0%, #a9c9ea 22%, var(--photo-brick) 45%, #9a5e44 62%, var(--photo-green) 85%);
  }
  .photo-small {
    top: 958px; width: 222px; height: 184px;
    background: linear-gradient(170deg, var(--photo-sky) 0%, var(--photo-brick) 35%, #a06a4f 55%, var(--photo-green) 80%);
  }
  .photo-small.left { left: 69px; }
  .photo-small.right { left: 309px; }

  .new-tab {
    position: absolute; left: 62px; top: 679px; width: 76px; height: 148px;
    background: linear-gradient(90deg, var(--navy), var(--royal));
    border-radius: 0 74px 74px 0;
  }
  .new-tab span {
    position: absolute; left: 38px; top: 74px;
    transform: translate(-50%, -50%) rotate(-90deg);
    color: #ffffff; font-size: 24px; letter-spacing: 6px; font-weight: 400;
  }

  .corner-ribbon { position: absolute; left: 428px; top: 641px; }

  .details { position: absolute; left: 567px; top: 645px; width: 200px; }
  .detail { margin-bottom: 14px; }
  .detail h2 {
    font-size: 19.5px; font-weight: 700; color: var(--heading-blue);
    line-height: 24px;
    border-bottom: 2px solid var(--rule);
    padding-bottom: 1px; margin-bottom: 3px;
  }
  .detail p { font-size: 15px; line-height: 19px; }

  .footer-band {
    position: absolute; left: 0; top: 1173px; width: 844px; height: 27px;
    background: linear-gradient(90deg, var(--navy), var(--royal));
  }
</style>
</head>
<body>
<main class="cover">
  <svg class="header-band" width="844" height="620" viewBox="0 0 844 620" aria-hidden="true">
    <defs>
      <linearGradient id="headerGradient" x1="0" y1="0" x2="1" y2="0">
        <stop offset="0" stop-color="#23205f"/>
        <stop offset="1" stop-color="#1f55a8"/>
      </linearGradient>
    </defs>
    <path d="M0 0 H844 V592 C700 585 520 540 420 520 C340 505 300 490 250 510 C180 540 90 575 0 575 Z" fill="url(#headerGradient)"/>
    <path d="M0 566 C90 566 180 530 250 500 C300 480 340 494 420 512 C520 532 700 576 844 583" fill="none" stroke="#ffffff" stroke-width="3"/>
  </svg>

  <div class="brand-name">QUILLBROOK STAYS</div>

  <div class="contact">
    <p>18 Harbour Lane, Millford. Qld 4120 Po Box 312,</p>
    <p>Eastvale. Qld 4009 UK</p>
    <div class="gap"></div>
    <p>P. 08450 772 418</p>
    <p>E. mail@quillbrookstays.co.uk</p>
  </div>

  <div class="web">www.<strong>quillbrookstays</strong>.co.uk</div>

  <div class="photo photo-main" role="img" aria-label="Photograph of the property: brick apartment building with trees"></div>
  <div class="new-tab"><span>NEW</span></div>
  <svg class="corner-ribbon" width="110" height="110" viewBox="0 0 110 110" aria-hidden="true">
    <defs>
      <linearGradient id="ribbonGradient" x1="0" y1="0" x2="1" y2="1">
        <stop offset="0" stop-color="#1f55a8"/>
        <stop offset="1" stop-color="#23205f"/>
      </linearGradient>
    </defs>
    <path d="M58 12 L80 0 L100 36 Z" fill="#1b1a4f"/>
    <path d="M52 12 L80 12 L102 40 L102 96 Z" fill="url(#ribbonGradient)"/>
  </svg>

  <div class="photo photo-small left" role="img" aria-label="Photograph of the property exterior"></div>
  <div class="photo photo-small right" role="img" aria-label="Photograph of the property exterior"></div>

  <section class="details">
    <div class="detail">
      <h2>Property Address</h2>
      <p>24 Linden Court, Ashby<br>Road, Oakhurst<br>Surrey KT22 4RW</p>
    </div>
    <div class="detail">
      <h2>Property Size</h2>
      <p>2 Bedroom Furnished<br>Flat Check Out</p>
    </div>
    <div class="detail">
      <h2>Job Type</h2>
      <p>For Sale</p>
    </div>
    <div class="detail">
      <h2>Agent Name</h2>
      <p>Mark Ellison</p>
    </div>
    <div class="detail">
      <h2>Date</h2>
      <p>10th July 2013</p>
    </div>
  </section>

  <div class="footer-band"></div>
</main>
</body>
</html>
```